Brochure for community platform NGO needed

We are a non-profit working on building the first community platform for refugees, supporters and organisations all over Europe to facilitate inclusion on a community level.

We need a brochure with nice design to show to other organisations, donors, etc.

The design should show our emphasis on community, participation, humanity and empowerment. It should communicate trustworthiness, optimism and equality.

Target Market(s)

locals and organisations supporting refugees in europe

Industry/Entity Type

Non-Profit

Requirements
Must have
• our logo
Nice to have
• design representing the idea - something with bridges or puzzle pieces, something showing community, diversity, participation, etc.
Should not have
• stereotypical representations

```html
<!DOCTYPE html>
<html lang="en">
<head>
<meta charset="utf-8">
<title>Pontora – Brochure Spread</title>
<link href="https://fonts.googleapis.com/css2?family=Josefin+Sans:wght@300;400;700&family=Open+Sans:ital,wght@0,400;0,700;1,700&family=Anton&display=swap" rel="stylesheet">
<style>
  :root {
    --navy: #1e2d5e;
    --gold: #d1a824;
    --charcoal: #4a4442;
    --stone: #a19796;
    --paper: #ededed;
    --backdrop: #dcdcdc;
    --photo-light: #6fa0d8;
    --photo-deep: #1f5fb8;
  }
  html, body {
    margin: 0;
    padding: 0;
    width: 1200px;
    height: 1027px;
    overflow: hidden;
    background: var(--backdrop);
  }
  .spread {
    position: absolute;
    left: 40px;
    top: 117px;
    width: 1120px;
    height: 792px;
    display: flex;
    box-shadow: 0 8px 24px rgba(0,0,0,0.18);
  }
  .page { width: 560px; height: 792px; display: block; }
  .headline { font-family: "Josefin Sans", sans-serif; font-weight: 300; }
  .body-copy { font-family: "Open Sans", sans-serif; font-size: 10.5px; fill: #4a4a4a; }
  .body-copy .lead { font-weight: 700; font-style: italic; fill: var(--navy); }
  .web { font-family: "Josefin Sans", sans-serif; font-weight: 400; letter-spacing: 5px; }
  .brand { font-family: "Josefin Sans", sans-serif; font-weight: 700; fill: var(--navy); }
  .slogan-big { font-family: "Anton", sans-serif; fill: var(--navy); }
</style>
</head>
<body>
<main class="spread">

  <!-- Back cover -->
  <svg class="page page-back" viewBox="0 0 560 792" xmlns="http://www.w3.org/2000/svg">
    <rect class="paper" width="560" height="792" fill="var(--paper)"/>
    <polygon class="top-wedge" points="60,0 560,0 560,175 130,175" fill="var(--navy)"/>
    <text class="web" x="340" y="150" font-size="15" fill="#fff" text-anchor="middle">www.pontora.eu</text>
    <rect class="side-bar" x="0" y="150" width="42" height="350" fill="var(--gold)"/>

    <rect class="heading-band" x="130" y="195" width="430" height="52" fill="var(--gold)"/>
    <polygon class="heading-fold" points="130,247 145,247 130,258" fill="var(--navy)"/>
    <text class="headline" x="145" y="231" font-size="24" fill="#fff">WHAT CAN YOU DO ?</text>

    <text class="body-copy">
      <tspan x="140" y="275">There are many ways to participate and help building the very</tspan>
      <tspan x="140" y="289">first community platform for refugees and supporters:</tspan>
      <tspan x="140" y="312" fill="var(--navy)">▸ </tspan><tspan class="lead">Donate:</tspan><tspan> we have 50.000 Euros available so far, but that won't</tspan>
      <tspan x="152" y="326">get us all the way to finalise the platform. Every Euro counts!</tspan>
      <tspan x="140" y="346" fill="var(--navy)">▸ </tspan><tspan class="lead">Spread the word:</tspan><tspan> PONTORA relies on a strong community –</tspan>
      <tspan x="152" y="360">the more, the better!</tspan>
      <tspan x="140" y="380" fill="var(--navy)">▸ </tspan><tspan class="lead">Join our Team:</tspan><tspan> you are super motivated and want to donate</tspan>
      <tspan x="152" y="394">your time and work for the greater purpose? Awesome! We</tspan>
      <tspan x="152" y="408">are always on the lookout for enthusiastic people to join our</tspan>
      <tspan x="152" y="422">team!</tspan>
      <tspan x="140" y="442" fill="var(--navy)">▸ </tspan><tspan class="lead">Sponsor us:</tspan><tspan> You own a company and would like to do good</tspan>
      <tspan x="152" y="456">while at the same time attracting new customers? Check out</tspan>
      <tspan x="152" y="470">our sponsorship options!</tspan>
    </text>

    <rect class="charcoal-band" x="502" y="290" width="58" height="270" fill="var(--charcoal)"/>

    <text class="headline" x="120" y="610" font-size="30" fill="var(--navy)">SUPPORT OUR COMMUNITY</text>

    <circle cx="206" cy="653" r="9" fill="var(--navy)"/>
    <text class="brand" x="222" y="664" font-size="30">pontora</text>

    <rect class="footer-band" x="0" y="705" width="560" height="87" fill="var(--navy)"/>
    <text class="headline" x="130" y="757" font-size="17" fill="#fff">CALL US</text>
    <text class="headline" x="215" y="757" font-size="17" fill="#fff">+43 1 000 45 67</text>
  </svg>

  <!-- Front cover -->
  <svg class="page page-front" viewBox="0 0 560 792" xmlns="http://www.w3.org/2000/svg">
    <defs>
      <linearGradient id="photoTone" x1="0" y1="0" x2="1" y2="1">
        <stop offset="0" stop-color="var(--photo-light)"/>
        <stop offset="1" stop-color="var(--photo-deep)"/>
      </linearGradient>
    </defs>
    <rect class="paper" width="560" height="792" fill="var(--paper)"/>
    <rect class="top-sliver" x="0" y="0" width="40" height="175" fill="var(--navy)"/>

    <circle cx="318" cy="150" r="12" fill="var(--navy)"/>
    <text class="brand" x="338" y="165" font-size="46">pontora</text>

    <rect class="navy-strip" x="230" y="255" width="330" height="60" fill="var(--navy)"/>
    <polygon class="gold-band" points="0,195 380,255 380,315 0,315" fill="var(--gold)"/>
    <text class="headline" x="95" y="300" font-size="22" fill="#fff">BUILDING COMMUNITY</text>

    <polygon class="stone-wedge" points="380,315 420,315 430,375" fill="var(--stone)"/>
    <rect class="navy-corner" x="430" y="315" width="130" height="90" fill="var(--navy)"/>

    <polygon class="charcoal-wedge" points="0,300 200,315 0,560" fill="var(--charcoal)"/>
    <polygon class="navy-diagonal" points="0,560 220,315 380,315 150,640 0,640" fill="var(--navy)"/>

    <polygon class="photo" role="img" aria-label="Photo of a young child drinking from a bottle in front of a blue tent" points="260,340 430,380 560,400 560,640 150,640" fill="url(#photoTone)"/>

    <rect class="gold-base" x="0" y="640" width="560" height="152" fill="var(--gold)"/>
    <polygon class="navy-footer" points="130,640 560,640 560,690 160,690" fill="var(--navy)"/>
    <text class="headline" x="540" y="682" font-size="13" fill="#fff" text-anchor="end">info@pontora.eu</text>

    <rect class="charcoal-block" x="205" y="698" width="260" height="46" fill="var(--charcoal)"/>
    <text class="web" x="335" y="728" font-size="18" fill="#fff" text-anchor="middle">www.pontora.eu</text>

    <text class="headline" x="190" y="748" font-size="22" fill="var(--navy)" text-anchor="end">UNITED</text>
    <text class="headline" x="190" y="774" font-size="22" fill="var(--navy)" text-anchor="end">FOR</text>
    <text class="slogan-big" x="200" y="780" font-size="40">HUMANITY</text>
  </svg>

</main>
</body>
</html>
```